Blog

Need a simple blog where questions can be posted and answered by the community. I already have something started in WordPress. www.orchidtrailhub.com. I cannot figure out how to make the blog functionality work the way I want. It is IMPORTANT the designer code it in the existing wordpress account.

```html
<!DOCTYPE html>
<html lang="en">
<head>
<meta charset="utf-8">
<title>Orchid Trail Partner &amp; Industry Forum</title>
<link href="https://fonts.googleapis.com/css2?family=Lato:wght@400;700&display=swap" rel="stylesheet">
<style>
:root{
  --navy:#2f3a6e;
  --brand-blue:#3a63a8;
  --nav-blue:#3d6cb3;
  --button-blue:#7f9fd4;
  --hero-dark:#1d3c77;
  --hero-mid:#2f5a9a;
  --page-grey:#efefef;
  --line:#c9cbd3;
  --text:#2b2b2b;
  --muted:#6b6b6b;
  --accent-red:#d0021b;
  --icon-blue:#2a8fd8;
  --icon-orange:#e8892f;
  --stat-bg:#ededed;
  --footer:#37355e;
  --white:#ffffff;
}
*{box-sizing:border-box;margin:0;padding:0}
html,body{width:965px;height:1200px;overflow:hidden}
body{font-family:'Lato',sans-serif;color:var(--text);background:var(--page-grey);position:relative}

/* header */
.site-header{position:absolute;left:0;top:0;width:965px;height:104px;background:var(--white)}
.brand{position:absolute;left:92px;top:24px;display:flex;align-items:center;gap:12px}
.brand-mark{width:44px;height:44px;background:var(--navy)}
.brand-name{font-weight:700;font-size:15px;line-height:17px;color:var(--navy)}
.brand-name span{display:block;color:var(--brand-blue)}
.main-nav{position:absolute;top:32px;left:482px;height:40px;font-size:14px;color:#444}
.main-nav a{text-decoration:none;color:inherit;position:absolute;top:0;height:40px;line-height:40px;white-space:nowrap}
.main-nav .active{color:var(--nav-blue);left:0}
.main-nav .active::after{content:"";position:absolute;left:0;right:0;top:69px;height:3px;background:var(--button-blue)}
.nav-about{left:78px}
.nav-questions{left:163px}
.nav-ask{left:266px;width:132px;text-align:center;background:var(--button-blue);color:var(--white)!important}

/* hero */
.hero{position:absolute;left:0;top:104px;width:965px;height:302px;color:var(--white);text-align:center}
.hero-backdrop{position:absolute;inset:0;background:radial-gradient(circle at 30% 40%,var(--hero-mid),var(--hero-dark) 75%)}
.hero-title{position:relative;font-weight:700;font-size:23px;line-height:37px;padding-top:52px;width:790px;margin:0 auto}
.hero-sub{position:relative;font-weight:700;font-size:18px;line-height:25px;margin:28px auto 0;width:730px}
.follow-btn{position:relative;display:inline-flex;align-items:center;gap:8px;margin-top:15px;height:34px;padding:0 11px;border:1px solid var(--white);font-size:12px;color:var(--white)}
.follow-btn i{width:12px;height:12px;background:var(--white);display:block}

/* questions */
.questions{position:absolute;left:90px;top:446px;width:521px}
.section-head{display:flex;align-items:center;height:17px}
.section-head h2{font-size:17px;font-weight:700;color:var(--navy);white-space:nowrap}
.section-head .rule{flex:1;height:1px;background:#8b8fa8;margin:0 11px 0 12px}
.filter{font-size:9px;color:var(--muted);display:flex;gap:8px;white-space:nowrap}
.filter b{color:var(--navy)}
.filter .on{position:relative;color:var(--muted)}
.filter .on::after{content:"";position:absolute;left:0;right:0;bottom:-4px;height:2px;background:var(--accent-red)}
.search{margin-top:19px;height:31px;background:var(--white);border:1px solid var(--line);display:flex;align-items:center;justify-content:space-between;padding:0 9px;font-size:11px;color:#8a8a8a}
.question-list{margin-top:15px;background:var(--white);border:1px solid var(--line)}
.question{height:104px;border-bottom:1px solid var(--line);position:relative}
.q-icon{position:absolute;left:23px;top:20px;width:37px;height:37px;border-radius:50%;border:1.5px solid;display:flex;align-items:center;justify-content:center}
.q-icon.answered{border-color:var(--icon-blue)}
.q-icon.open{border-color:var(--icon-orange);color:var(--icon-orange);font-weight:700;font-size:15px}
.q-text{position:absolute;left:74px;top:19px;width:264px;font-size:10px;line-height:12.5px}
.q-meta{position:absolute;left:73px;top:71px;display:flex;align-items:center;gap:5px;font-size:8.5px;color:var(--muted)}
.q-meta i{width:17px;height:17px;border-radius:50%;border:1px solid var(--line);display:block}
.q-meta em{font-style:normal;color:var(--accent-red)}
.stats{position:absolute;left:377px;top:19px;display:flex;gap:6px}
.stat{width:36px;text-align:center}
.stat b{display:flex;width:36px;height:36px;border-radius:50%;background:var(--stat-bg);align-items:center;justify-content:center;font-size:10px;color:var(--brand-blue)}
.stat span{display:block;margin-top:8px;font-size:8.5px;color:var(--muted);white-space:nowrap;margin-left:-6px;margin-right:-6px}
.pager{height:35px;background:#e8e8e8;display:flex;justify-content:center;align-items:center;gap:13px;font-size:11px;color:#444}
.pager .current{border-bottom:2px solid var(--accent-red);padding-bottom:1px}

/* sidebar */
.sidebar{position:absolute;left:634px;top:446px;width:238px;height:600px;background:var(--white);border:1px solid var(--line)}
.ask-btn{margin:17px 0 0 15px;width:206px;height:40px;background:var(--brand-blue);color:var(--white);font-weight:700;font-size:13px;display:flex;align-items:center;justify-content:center;gap:6px}
.send-note{margin:13px 14px 0;text-align:center;font-size:10px;line-height:13px}
.news-head{display:flex;align-items:center;margin:19px 21px 0 18px;font-size:12.5px;font-weight:700;color:var(--navy)}
.news-head::after{content:"";flex:1;height:1px;background:var(--button-blue);margin-left:10px}
.news{list-style:none;margin:14px 25px 0 18px}
.news li{font-size:11.5px;line-height:14px;padding:6px 0 6px 1px;border-bottom:1px solid #ddd;color:#333}
.news li:last-child{border-bottom:none}

/* footer */
.site-footer{position:absolute;left:0;top:1112px;width:965px;height:88px;background:var(--footer);color:var(--white);font-size:13px;text-align:center;line-height:88px}
</style>
</head>
<body>
<header class="site-header">
  <div class="brand">
    <div class="brand-mark"></div>
    <div class="brand-name">ORCHID TRAIL<span>PARTNER &amp; INDUSTRY FORUM</span></div>
  </div>
  <nav class="main-nav">
    <a class="active" href="#">HOME</a>
    <a class="nav-about" href="#">ABOUT</a>
    <a class="nav-questions" href="#">QUESTIONS</a>
    <a class="nav-ask" href="#">ASK A QUESTION</a>
  </nav>
</header>

<section class="hero">
  <div class="hero-backdrop" role="img" aria-label="Deep blue background of magnified virus particles"></div>
  <h1 class="hero-title">This site is designed for our valued partners and industry associates to connect and share COVID-19 information.</h1>
  <p class="hero-sub">Be sure to check out our network page! There is more information from many more contributors</p>
  <div class="follow-btn"><i></i>Follow our network</div>
</section>

<main class="questions">
  <div class="section-head">
    <h2>ALL QUESTIONS</h2>
    <div class="rule"></div>
    <div class="filter"><b>Filter:</b><span class="on">All</span><span>Open</span><span>Closed</span><span>Unanswered</span></div>
  </div>
  <div class="search">What do you want to know?
    <svg width="16" height="16" viewBox="0 0 16 16" fill="none" stroke="#333" stroke-width="1.3"><circle cx="9.5" cy="6.5" r="5"/><line x1="6" y1="10" x2="1.5" y2="14.5"/></svg>
  </div>

  <div class="question-list">
    <article class="question">
      <div class="q-icon answered"><svg width="16" height="13" viewBox="0 0 16 13"><path d="M6 1 1 5.5 6 10V7c4 0 6.5 1 8.5 4.5C14 7 11.5 4 6 4z" fill="var(--icon-blue)"/></svg></div>
      <p class="q-text">What measures are you taking when forced by a state to take back a resident sent to the hospital and subsequently diagnosed with COVID19?</p>
      <div class="q-meta"><i></i>by <em>admin</em> asked 2 dayes ago</div>
      <div class="stats"><div class="stat"><b>20</b><span>Views</span></div><div class="stat"><b>3</b><span>Answers</span></div><div class="stat"><b>10</b><span>Votes</span></div></div>
    </article>
    <article class="question">
      <div class="q-icon open">?</div>
      <p class="q-text">How do we protect against a potential land grab by unions leveraging this time as an opportunity to grab members?</p>
      <div class="q-meta"><i></i>by <em>admin</em> asked 3 dayes ago</div>
      <div class="stats"><div class="stat"><b>11</b><span>Views</span></div><div class="stat"><b>1</b><span>Answers</span></div><div class="stat"><b>0</b><span>Votes</span></div></div>
    </article>
    <article class="question">
      <div class="q-icon answered"><svg width="16" height="13" viewBox="0 0 16 13"><path d="M6 1 1 5.5 6 10V7c4 0 6.5 1 8.5 4.5C14 7 11.5 4 6 4z" fill="var(--icon-blue)"/></svg></div>
      <p class="q-text">What measures are you taking when forced by a state to take back a resident sent to the hospital and subsequently diagnosed with COVID19?</p>
      <div class="q-meta"><i></i>by <em>admin</em> asked 5 dayes ago</div>
      <div class="stats"><div class="stat"><b>8</b><span>Views</span></div><div class="stat"><b>3</b><span>Answers</span></div><div class="stat"><b>2</b><span>Votes</span></div></div>
    </article>
    <article class="question">
      <div class="q-icon open">?</div>
      <p class="q-text">How do we protect against a potential land grab by unions leveraging this time as an opportunity to grab members?</p>
      <div class="q-meta"><i></i>by <em>admin</em> asked 2 dayes ago</div>
      <div class="stats"><div class="stat"><b>11</b><span>Views</span></div><div class="stat"><b>1</b><span>Answers</span></div><div class="stat"><b>0</b><span>Votes</span></div></div>
    </article>
    <article class="question">
      <div class="q-icon answered"><svg width="16" height="13" viewBox="0 0 16 13"><path d="M6 1 1 5.5 6 10V7c4 0 6.5 1 8.5 4.5C14 7 11.5 4 6 4z" fill="var(--icon-blue)"/></svg></div>
      <p class="q-text">What measures are you taking when forced by a state to take back a resident sent to the hospital and subsequently diagnosed with COVID19?</p>
      <div class="q-meta"><i></i>by <em>admin</em> asked 2 dayes ago</div>
      <div class="stats"><div class="stat"><b>8</b><span>Views</span></div><div class="stat"><b>3</b><span>Answers</span></div><div class="stat"><b>2</b><span>Votes</span></div></div>
    </article>
    <nav class="pager">
      <svg width="8" height="12" viewBox="0 0 8 12" fill="none" stroke="var(--accent-red)" stroke-width="1.2"><path d="M7 1 1 6l6 5"/></svg>
      <span>1</span><span class="current">2</span><span>3</span><span>4</span>
      <svg width="8" height="12" viewBox="0 0 8 12" fill="none" stroke="var(--accent-red)" stroke-width="1.2"><path d="M1 1l6 5-6 5"/></svg>
    </nav>
  </div>
</main>

<aside class="sidebar">
  <div class="ask-btn"><svg width="11" height="11" viewBox="0 0 11 11"><path d="M5.5 0v11M0 5.5h11" stroke="#fff" stroke-width="2.2"/></svg>ASK YOUR QUESTION</div>
  <p class="send-note">Or send your questions to forum@orchidtrailhub.com and we will be sure to post them.</p>
  <div class="news-head">Latest News</div>
  <ul class="news">
    <li>Coronavirus (COVID-19) current situation and case numbers</li>
    <li>Coronavirus (COVID-19) health alert</li>
    <li>COVID-19 Information for workplaces</li>
    <li>COVID-19 (Coronavirus) statistics</li>
    <li>Information sharing on COVID-19 Meridian Care Alliance</li>
    <li>Coronavirus (COVID-19) events as they happen</li>
    <li>COVID-19 (Coronavirus) statistics</li>
    <li>COVID-19 Information for workplaces</li>
    <li>Coronavirus (COVID-19) current situation and case numbers</li>
  </ul>
</aside>

<footer class="site-footer">© Copyright 2020 ORCHID TRAIL PARTNER &amp; INDUSTRY FORUM. All Rights Reserved</footer>
</body>
</html>
```